Banner Ads for Online Poker Promotion

We are an online poker network, the Oskarn (www.thekrx.eu). We are looking for a small selection of web banner ads for our latest promotion and we are trying crowdsourcing for the first time!

Banner sizes that we need are:
- 196x523 (static .psd and .png)
- 199x129 (static .psd and .png)
- 447x426 (static .psd and .png)
- 500x400 (static .psd and .png)
- 697x167 (static .psd and .png)
- 460x60 (animated .gif)

The promotion name is ‘Late Rush’ and the concept is that a person who enters one of the specified tournaments four or more times during the promotion will win a free ticket to play that tournament again. So effectively a ‘Rush Late, Bag a Seat’ promo. We also are giving away €10,000 in free entries to the tournaments during the promotion. The specific tournaments are called ‘Calm Dawn Out’ and ‘The Sun Deck’ and run daily on our network. The promotion runs October 1 – 31.

Guidelines:

The name of the promotion, ‘Late Rush’, should feature prominently in the banners.

The strap line can be ‘Rush Late, Bag a Seat’ or something that encourages players to ‘take a shot’ at the tournaments.

Our network logo may feature, but is not absolutely necessary.

Examples of past promotional imagery can be found on our website, in particular these pages: http://www.thekrx.eu/promotions/ and http://www.thekrx.eu/promotions/archived-promotions/

We are looking to go in a more modern and risqué direction than the past, in order to stand out from competition which is very bland.

Please do not use common poker imagery – so no cards, chips, suit icons etc – or objects associated with live poker (tables, etc). This sort of imagery is too clichéd.

More like iOS7, less like iOS6

Think glamour, neon, rock music, extreme sports, and the Soft Tide!

If any further guidance is needed please don’t hesitate to ask.

```html
<!DOCTYPE html>
<html lang="en">
<head>
<meta charset="utf-8">
<title>Late Rush – Oskarn Promotion Banner</title>
<link rel="stylesheet" href="https://fonts.googleapis.com/css2?family=Pacifico&family=Questrial&family=Didact+Gothic&display=swap">
<style>
  :root {
    --sky-top: #b9bdb4;
    --sky-mid: #8e9690;
    --city-low: #3c4648;
    --city-deep: #1e2629;
    --white: #ffffff;
    --band: rgba(255, 255, 255, 0.82);
    --band-text: #4a4c4e;
    --logo: rgba(255, 255, 255, 0.78);
  }
  html, body {
    margin: 0;
    padding: 0;
    overflow: hidden;
    background: #ffffff;
  }
  .banner {
    position: relative;
    width: 1200px;
    height: 1197px;
    overflow: hidden;
    font-family: "Questrial", "Didact Gothic", sans-serif;
  }
  .city-backdrop {
    position: absolute;
    inset: 0;
    background:
      linear-gradient(90deg, rgba(30,38,41,0.25) 0%, rgba(30,38,41,0) 30%, rgba(30,38,41,0) 70%, rgba(30,38,41,0.3) 100%),
      linear-gradient(180deg, var(--sky-top) 0%, var(--sky-mid) 28%, #6c7774 45%, var(--city-low) 70%, var(--city-deep) 100%);
  }
  .promo-title {
    position: absolute;
    left: 0;
    right: 0;
    top: 30px;
    margin: 0;
    text-align: center;
    font-family: "Pacifico", cursive;
    font-weight: 400;
    font-size: 200px;
    line-height: 230px;
    color: var(--white);
    text-shadow: 0 2px 6px rgba(0,0,0,0.12);
  }
  .promo-title span { display: block; }
  .strap-band {
    position: absolute;
    left: 0;
    right: 0;
    top: 562px;
    height: 253px;
    background: var(--band);
    display: flex;
    flex-direction: column;
    justify-content: center;
    align-items: center;
  }
  .strap-line {
    margin: 0;
    font-family: "Didact Gothic", "Questrial", sans-serif;
    font-size: 78px;
    line-height: 112px;
    color: var(--band-text);
    text-align: center;
    letter-spacing: -0.5px;
  }
  .strap-line strong {
    font-weight: 700;
    -webkit-text-stroke: 1.4px var(--band-text);
  }
  .call-to-action {
    position: absolute;
    left: 0;
    right: 0;
    top: 870px;
    margin: 0;
    text-align: center;
    font-size: 54px;
    line-height: 70px;
    color: var(--white);
  }
  .network-mark {
    position: absolute;
    left: 50px;
    bottom: 40px;
    display: flex;
    align-items: center;
    gap: 14px;
    font-family: "Questrial", sans-serif;
    font-size: 42px;
    letter-spacing: 2px;
    color: var(--logo);
  }
  .network-mark .mark-square {
    width: 18px;
    height: 18px;
    background: var(--logo);
  }
</style>
</head>
<body>
  <main class="banner">
    <div class="city-backdrop" role="img" aria-label="Hazy aerial view of a city skyline with tall towers"></div>

    <h1 class="promo-title"><span>Late</span><span>Rush</span></h1>

    <section class="strap-band">
      <p class="strap-line">Rush <strong>Late</strong></p>
      <p class="strap-line">Bag <strong>a Seat</strong></p>
    </section>

    <p class="call-to-action">Try your luck today!</p>

    <div class="network-mark">
      <span class="mark-square"></span>
      <span class="mark-name">Oskarn</span>
    </div>
  </main>
</body>
</html>
```